Delta Ridge Arms

Firearms Website

Requirements
Must have
• we are looking for two or three pages for a new company we are starting. The Name is Delta Ridge Arms. The site will be DeltaRidgeArms.example (nothing on site at this time) We will be selling mainly handguns and products for self defense. We want this site to focus on the handgun and ammo sells as well as low cost transfers. we will handle the ecommerce part) We want a

1.) main page, mainly general information on the company.

2.) a page for sells. we will be adding the guns by hand as we place them for sell and use our credit card process. We just need the layout to fill in the items for sale on this page.

3.) navigation will be.. HOME - SALES (((guns and gun Accessories)) and self defense products) - Contact US- Transfers

company info

Delta Ridge Arms

DeltaRidgeArms.example

sales@DeltaRidgeArms.example

855-Bolt 2 Save (855-265-2728) same number for fax

412 south Walnut street

Kosciusko, ms. 39090

```html
<!DOCTYPE html>
<html lang="en">
<head>
<meta charset="utf-8">
<title>Delta Ridge Arms</title>
<link href="https://fonts.googleapis.com/css2?family=PT+Sans+Narrow:wght@400;700&family=PT+Sans:wght@400;700&display=swap" rel="stylesheet">
<style>
  :root {
    --page: #f1f1f1;
    --navy: #1d4c78;
    --blue: #1a9ad6;
    --blue-dark: #0a6fb5;
    --blue-light: #37b3ea;
    --text: #222;
    --muted: #444;
    --line: #d4d4d4;
    --card: #f6f6f6;
    --hero-grey: #8b8589;
    --white: #fff;
  }
  * { box-sizing: border-box; margin: 0; padding: 0; }
  html, body { width: 1200px; height: 1015px; overflow: hidden; }
  body {
    position: relative;
    background: var(--page);
    font-family: "PT Sans", sans-serif;
    color: var(--text);
    border-top: 2px solid var(--blue-dark);
  }
  .abs { position: absolute; }
  .display { font-family: "PT Sans Narrow", sans-serif; }

  .brand { left: 162px; top: 12px; font-size: 27px; color: var(--navy); letter-spacing: -0.2px; }
  .phone { left: 790px; top: 12px; display: flex; align-items: center; gap: 7px; }
  .phone-icon { width: 32px; height: 32px; border-radius: 50%; background: var(--blue-light); display: flex; align-items: center; justify-content: center; }
  .phone-text { font-size: 18px; color: var(--navy); }

  .main-nav { left: 164px; top: 53px; width: 601px; height: 28px; display: flex;
    background: linear-gradient(#33aee8, #0b79c2); border-radius: 2px; box-shadow: 0 2px 3px rgba(0,0,0,.25); }
  .main-nav a { flex: 1; color: var(--white); text-decoration: none; font-family: "PT Sans Narrow", sans-serif;
    font-size: 17px; text-align: center; line-height: 28px; border-right: 1px solid #0c6aa8; }
  .main-nav a:last-child { border-right: none; }

  .search { left: 828px; top: 53px; width: 210px; height: 28px; background: var(--white);
    border: 1px solid #d6d6d6; border-radius: 3px; box-shadow: 0 1px 2px rgba(0,0,0,.1); }
  .search span { position: absolute; left: 8px; top: 5px; font-size: 12px; color: #555; }
  .search-btn { position: absolute; right: 5px; top: 5px; width: 19px; height: 17px; background: var(--blue-dark);
    border-radius: 2px; display: flex; align-items: center; justify-content: center; }

  .hero { left: 165px; top: 96px; width: 875px; height: 327px; border-radius: 3px; overflow: hidden;
    background: linear-gradient(90deg, var(--hero-grey) 0, var(--hero-grey) 42%, #a09ca2 55%, #6e6a72 80%, #8d8a90 100%);
    box-shadow: 0 10px 10px -4px rgba(0,0,0,.45); }
  .hero-title { position: absolute; left: 41px; top: 74px; font-size: 58px; line-height: 58px; color: var(--white); font-weight: 400; }
  .hero-dots { position: absolute; left: 45px; top: 272px; display: flex; gap: 5px; }
  .hero-dots i { width: 12px; height: 12px; border-radius: 50%; background: #e9e9e9; display: block; }
  .hero-dots i.active { background: var(--blue-light); box-shadow: inset 0 0 0 2px #e9e9e9; }

  .card { top: 453px; width: 285px; height: 178px; background: var(--card); border: 1px solid #dcdcdc; border-radius: 3px; }
  .card h2 { position: absolute; left: 14px; top: 10px; font-size: 22px; font-weight: 400; color: var(--blue); }
  .card-photo { position: absolute; left: 15px; top: 46px; width: 108px; height: 110px; border: 1px solid #cfcfcf; border-radius: 4px; }
  .card p { position: absolute; left: 136px; top: 45px; width: 133px; font-size: 13px; line-height: 21px; text-align: justify; }
  .btn { display: inline-block; background: linear-gradient(#27a6e4, #0a72bb); color: var(--white);
    font-family: "PT Sans Narrow", sans-serif; font-weight: 700; font-size: 12px; text-align: center;
    border-radius: 2px; box-shadow: 0 2px 2px rgba(0,0,0,.25); }
  .card .btn { position: absolute; left: 136px; top: 156px; width: 68px; height: 22px; line-height: 22px; }

  .section-title { font-size: 22px; font-weight: 400; color: var(--blue); }
  .news-item { left: 164px; width: 502px; }
  .news-item .bullet { position: absolute; left: 0; top: 3px; width: 12px; height: 12px; border: 1px solid #888; border-radius: 50%; }
  .news-item .bullet::after { content: ""; position: absolute; left: 3.5px; top: 2.5px; border-left: 4px solid #666; border-top: 2.5px solid transparent; border-bottom: 2.5px solid transparent; }
  .news-item p { margin-left: 26px; font-size: 12px; line-height: 18.5px; color: var(--text); }
  .news-item a { display: block; margin-left: 25px; margin-top: 2px; font-size: 12px; color: var(--blue-dark); text-decoration: none; }
  .news-rule { left: 166px; top: 759px; width: 500px; height: 1px; background: var(--line); }
  .col-rule { left: 696px; top: 661px; width: 1px; height: 180px; background: var(--line); }

  .field-label { left: 725px; font-size: 11px; color: var(--text); }
  .field { left: 727px; width: 300px; height: 28px; background: var(--white); border: 1px solid #bdbdbd; }
  .subscribe { left: 730px; top: 810px; width: 67px; height: 22px; line-height: 22px; font-size: 13px; }

  .footer { left: 168px; top: 862px; width: 879px; height: 153px; background: var(--white); box-shadow: 0 0 3px rgba(0,0,0,.2); }
  .follow { position: absolute; left: 0; right: 0; top: 18px; text-align: center; font-family: "PT Sans Narrow", sans-serif; font-size: 14px; color: var(--blue-dark); }
  .social { position: absolute; left: 394px; top: 43px; display: flex; gap: 7px; }
  .social span { width: 20px; height: 20px; border-radius: 2px; display: block; }
  .footer-rule { position: absolute; left: 0; right: 0; top: 74px; height: 1px; background: var(--line); }
  .footer-links { position: absolute; left: 0; right: 0; top: 92px; text-align: center; font-size: 11px; color: var(--text); word-spacing: 2px; }
  .copyright { position: absolute; left: 0; right: 0; top: 114px; text-align: center; font-size: 11px; color: var(--text); }
</style>
</head>
<body>

<header>
  <div class="abs brand display">DELTA RIDGE ARMS</div>
  <div class="abs phone">
    <div class="phone-icon">
      <svg width="16" height="18" viewBox="0 0 16 18"><path d="M3 1 L6 1 L7 5 L5 7 C6 10 8 12 10 13 L12 11 L15 12 L15 16 C15 17 14 17 13 17 C6 16 1 10 1 3 C1 2 2 1 3 1 Z" fill="#fff"/></svg>
    </div>
    <div class="phone-text display">855-BOLT 2 SAVE OR &nbsp;(855-265-2728)</div>
  </div>
  <nav class="abs main-nav">
    <a href="#">HOME</a><a href="#">SALES</a><a href="#">SELF DEFENCE</a><a href="#">CONTACT US</a><a href="#">TRANSFERS</a>
  </nav>
  <div class="abs search">
    <span>Search</span>
    <div class="search-btn">
      <svg width="11" height="11" viewBox="0 0 11 11"><circle cx="4.5" cy="4.5" r="3.3" fill="none" stroke="#fff" stroke-width="1.6"/><line x1="7" y1="7" x2="10" y2="10" stroke="#fff" stroke-width="1.8"/></svg>
    </div>
  </div>
</header>

<section class="abs hero">
  <div role="img" aria-label="Photo of a semi-automatic handgun and its magazine on a reflective grey surface" style="position:absolute;left:360px;top:0;width:515px;height:327px;background:linear-gradient(135deg,#9a979e,#4d4a52 55%,#7d7a82);"></div>
  <h1 class="hero-title display">WELCOME TO<br>OUR SITE</h1>
  <div class="hero-dots"><i></i><i></i><i class="active"></i><i></i><i></i></div>
</section>

<article class="abs card" style="left:166px">
  <h2 class="display">ABOUT US</h2>
  <div class="card-photo" role="img" aria-label="Photo of a man in a hat and suit aiming a handgun" style="background:linear-gradient(135deg,#f4f4f4,#9a9a9a 60%,#eaeaea);"></div>
  <p>Lorem Ipsum is simply dummy text of the print-ing and typesetting industry. Lorem Ipsum has been...</p>
  <span class="btn">READ MORE</span>
</article>

<article class="abs card" style="left:462px">
  <h2 class="display">SALES</h2>
  <div class="card-photo" role="img" aria-label="Photo of hands holding a handgun against a dark background" style="background:radial-gradient(circle at 55% 60%,#5c5a5a,#111 70%);"></div>
  <p>Lorem Ipsum is simply dummy text of the print-ing and typesetting industry. Lorem Ipsum has been...</p>
  <span class="btn">READ MORE</span>
</article>

<article class="abs card" style="left:755px">
  <h2 class="display">SELF DEFENCE</h2>
  <div class="card-photo" role="img" aria-label="Photo of a handgun and cartridges on a wooden table" style="background:linear-gradient(135deg,#c0653e,#9a4a2a 60%,#c87550);"></div>
  <p>Lorem Ipsum is simply dummy text of the print-ing and typesetting industry. Lorem Ipsum has been...</p>
  <span class="btn">READ MORE</span>
</article>

<section>
  <h2 class="abs section-title display" style="left:164px;top:654px">NEWS</h2>
  <div class="abs news-item" style="top:695px">
    <span class="bullet"></span>
    <p>Lorem Ipsum is simply dummy text of the printing and typesetting industry. Lorem Ipsum has been...</p>
    <a href="#">READ MORE &gt;&gt;</a>
  </div>
  <div class="abs news-rule"></div>
  <div class="abs news-item" style="top:770px">
    <span class="bullet"></span>
    <p>Contrary to popular belief, Lorem Ipsum is not simply random text. It has roots in a piece of classical &nbsp;Latin literature from 45 BC, making it over ...</p>
    <a href="#">READ MORE &gt;&gt;</a>
  </div>
  <div class="abs col-rule"></div>
</section>

<section>
  <h2 class="abs section-title display" style="left:723px;top:654px">NEWSLETTER SIGNUP</h2>
  <div class="abs field-label" style="top:693px">Enter the Name</div>
  <div class="abs field" style="top:710px"></div>
  <div class="abs field-label" style="top:756px">Enter the Email id</div>
  <div class="abs field" style="top:773px"></div>
  <span class="abs btn subscribe">SUBSCRIBE</span>
</section>

<footer class="abs footer">
  <div class="follow">Follow us on</div>
  <div class="social">
    <span style="background:#3b5b99"></span>
    <span style="background:#1477b5"></span>
    <span style="background:#3eaee6"></span>
    <span style="background:#f28a1e"></span>
  </div>
  <div class="footer-rule"></div>
  <div class="footer-links">Home &nbsp;|&nbsp; Sales &nbsp;|&nbsp; Self Defence &nbsp;|&nbsp; Contact us &nbsp;|&nbsp; Transfers</div>
  <div class="copyright">Copyrights @ 2013 All Rights Reserved</div>
</footer>

</body>
</html>
```